Tobias Wrenfield - Cinematographer

NEED:
I'm looking for a sleek, professional, modern business card that will give give the recipient the impression that they can trust their production will go smoothly by hiring me. I will bring creativity and knowledge to their shoot, so that we can create powerful images.
I am looking for a card with a strong style and design ethos that could be expanded to a website and a full visual/graphic/design entity for me.
ABOUT ME:
I am a mid-twenties cinematographer, I work on music video, narrative short, commercial, and corporate projects. I blend the science and artistry of cameras and filmmaking to tell a story. I'm an artist, a technician, and a manager.
DESIGN:
I like sleek, simple design. Black, dark grays, white, dark navy, steel blues, I love cyan, but also cyan and red. I am not a fan of earthy tones. I generally prefer modern, san-serif fonts over serifs. My old logo was based on an aperture, a multi-blade device at the back of a lens that controls how much light passes through, but I made it with so many colors, that it doesn't necessarily lend itself to a specific color-scheme or design ethos. I liked that the aperture design provided a sense of the technical requirements of my job. I'm a fan of matte business cards, but am open to plenty of specialty print processes to make an outstanding card.
ATTACHED FILES:
My Old Rainbox Aperture Logo, plus a few designs I've tried playing around with, but am not tied to. I AM OPEN TO NEW DESIGNS, DO NOT FEEL TIED TO THIS.
**I've pulled my old logo down from the attached files, and instead attached other business cards I like, so as not to mislead you where I would like to go.
INFO:
Name: Tobias Wrenfield
Job: Cinematographer
Email: tkwrenfield@quillbox.example
Phone: 503.618.2907
Website: tobiaswrenfield.example
Updates
I'm adding some images of other cards that I like, and removing my old logo, since I'm looking for something new, and don't want that old logo to push anyone a certain direction.

```html
<!DOCTYPE html>
<html lang="en">
<head>
<meta charset="utf-8">
<title>Tobias Wrenfield – Cinematographer Business Card</title>
<link rel="stylesheet" href="https://fonts.googleapis.com/css2?family=Quicksand:wght@500;600;700&display=swap">
<style>
  :root {
    --backdrop: #8d8e91;
    --card-light: #38393c;
    --card-dark: #161618;
    --ink: #ffffff;
    --accent-cyan: #1fb4ea;
    --icon: #e9e9ea;
  }
  * { box-sizing: border-box; margin: 0; padding: 0; }
  html, body {
    width: 1200px;
    height: 900px;
    overflow: hidden;
    background: var(--backdrop);
    font-family: "Quicksand", sans-serif;
  }
  .canvas {
    position: relative;
    width: 1200px;
    height: 900px;
  }
  .card {
    position: absolute;
    width: 560px;
    height: 320px;
    border-radius: 30px;
    background: linear-gradient(120deg, var(--card-light) 0%, var(--card-dark) 55%, #242527 100%);
    color: var(--ink);
    overflow: hidden;
  }
  /* Front of card */
  .card--front { left: 60px; top: 90px; }
  .front-identity {
    position: absolute;
    left: 30px;
    top: 50%;
    transform: translateY(-50%);
    display: flex;
    align-items: center;
    gap: 18px;
  }
  .front-identity__ring {
    width: 160px;
    height: 160px;
    border: 4px solid var(--ink);
    border-radius: 50%;
    flex: none;
  }
  .front-identity__name {
    font-weight: 600;
    font-size: 38px;
    white-space: nowrap;
  }
  /* Back of card */
  .card--back { left: 580px; top: 490px; }
  .back-heading {
    position: absolute;
    left: 40px;
    top: 40px;
  }
  .back-heading__name {
    font-weight: 700;
    font-size: 42px;
    line-height: 46px;
    white-space: nowrap;
  }
  .back-heading__role {
    font-weight: 600;
    font-size: 32px;
    line-height: 38px;
    margin-left: 22px;
    white-space: nowrap;
  }
  .back-heading__rule {
    position: absolute;
    left: 110px;
    top: 130px;
    width: 400px;
    height: 3px;
    background: var(--accent-cyan);
    border-radius: 2px;
    transform: rotate(-2.6deg);
    transform-origin: left center;
  }
  .contact-list {
    position: absolute;
    left: 168px;
    top: 178px;
    list-style: none;
  }
  .contact-list__item {
    display: flex;
    align-items: center;
    gap: 10px;
    font-weight: 600;
    font-size: 23px;
    line-height: 34px;
    white-space: nowrap;
  }
  .contact-list__icon {
    width: 22px;
    height: 22px;
    flex: none;
  }
</style>
</head>
<body>
<main class="canvas">

  <section class="card card--front" aria-label="Card front">
    <div class="front-identity">
      <span class="front-identity__ring"></span>
      <span class="front-identity__name">Tobias Wrenfield</span>
    </div>
  </section>

  <section class="card card--back" aria-label="Card back">
    <div class="back-heading">
      <h1 class="back-heading__name">Tobias Wrenfield</h1>
      <p class="back-heading__role">Cinematographer</p>
    </div>
    <span class="back-heading__rule"></span>

    <ul class="contact-list">
      <li class="contact-list__item">
        <svg class="contact-list__icon" viewBox="0 0 24 24" aria-hidden="true">
          <path fill="var(--icon)" d="M6.6 2.5c.6-.3 1.3-.1 1.6.5l2 3.6c.3.6.2 1.2-.3 1.6L8.4 9.4c1 2.4 3.2 4.6 5.6 5.6l1.2-1.5c.4-.5 1.1-.6 1.6-.3l3.6 2c.6.3.8 1 .5 1.6l-1.2 2.4c-.4.8-1.3 1.3-2.2 1.1C10.4 19 5 13.6 3.9 6.5c-.1-.9.3-1.8 1.1-2.2z"/>
        </svg>
        <span>503.618.2907</span>
      </li>
      <li class="contact-list__item">
        <svg class="contact-list__icon" viewBox="0 0 24 24" aria-hidden="true">
          <rect x="2" y="5" width="20" height="14" rx="1.5" fill="var(--icon)"/>
          <path d="M3 6.5l9 7 9-7M3 18l6.5-6M21 18l-6.5-6" fill="none" stroke="#1c1c1e" stroke-width="1.6"/>
        </svg>
        <span>tkwrenfield@quillbox.example</span>
      </li>
      <li class="contact-list__item">
        <svg class="contact-list__icon" viewBox="0 0 24 24" aria-hidden="true">
          <circle cx="12" cy="12" r="10" fill="var(--icon)"/>
          <g fill="none" stroke="#1c1c1e" stroke-width="1.4">
            <ellipse cx="12" cy="12" rx="4.2" ry="10"/>
            <path d="M2 12h20M3.5 7h17M3.5 17h17M12 2v20"/>
          </g>
        </svg>
        <span>www.tobiaswrenfield.example</span>
      </li>
    </ul>
  </section>

</main>
</body>
</html>
```